Book cover design for title:

KITE
Turning Crews into Clans.

Author Marla Voskin

This is my second book the first one is The Hum Building a Flourishing and Cooperative Workplace Growth Climate ( see cover on www.marlavoskin.com).

I am after a cover that echoes the title of The Hum, (ie big bold lettering for the word KITE but not necessarily the images on the front. Although stylised figures are more the style I am after than realist photos. Strong colours and bold statement.

It is about teams that are able to thrive in the complexity of the fast paced and disruptive nature of the world today. 21st century tribes who connect fast to purpose and to each other.

My LinkedIn Marla Voskin and my website give you a flavour of what I do and how I do it.

```html
<!DOCTYPE html>
<html lang="en">
<head>
<meta charset="utf-8">
<title>KITE – Turning Crews into Clans</title>
<link rel="stylesheet" href="https://fonts.googleapis.com/css2?family=Poppins:wght@800&family=Nunito:wght@900&family=Montserrat:wght@400&display=swap">
<style>
  :root {
    --backdrop: #e9e6e2;
    --paper: #ffffff;
    --cover-red: #c01f2f;
    --title-yellow: #fff200;
    --tie-blue: #2b3592;
    --author-blue: #2f3a8f;
  }
  html, body {
    margin: 0;
    width: 1200px;
    height: 900px;
    overflow: hidden;
    background: var(--backdrop);
  }
  .canvas {
    position: relative;
    width: 1200px;
    height: 900px;
  }
  .book-cover {
    position: absolute;
    left: 357px;
    top: 90px;
    width: 486px;
    height: 720px;
    background: var(--paper);
    overflow: hidden;
    box-shadow: 0 2px 6px rgba(0,0,0,0.12);
  }
  .title-banner {
    position: absolute;
    left: 0;
    top: 0;
    width: 486px;
    height: 245px;
    display: block;
  }
  .book-title {
    position: absolute;
    left: 0;
    right: 0;
    top: 62px;
    margin: 0;
    text-align: center;
    font-family: "Poppins", sans-serif;
    font-weight: 800;
    font-size: 118px;
    line-height: 1;
    letter-spacing: -2px;
    color: var(--title-yellow);
    text-shadow: -5px 5px 0 var(--paper);
  }
  .tribe-figures {
    position: absolute;
    left: 112px;
    top: 268px;
    width: 262px;
    height: 222px;
    background: linear-gradient(180deg, var(--cover-red) 0%, var(--cover-red) 55%, #a8283f 75%, var(--tie-blue) 100%);
    border-radius: 6px;
  }
  .book-subtitle {
    position: absolute;
    left: 0;
    right: 0;
    top: 506px;
    margin: 0;
    text-align: center;
    font-family: "Nunito", sans-serif;
    font-weight: 900;
    font-size: 22px;
    color: var(--cover-red);
  }
  .book-author {
    position: absolute;
    left: 28px;
    top: 656px;
    margin: 0;
    font-family: "Montserrat", sans-serif;
    font-weight: 400;
    font-size: 20px;
    letter-spacing: 0.5px;
    text-transform: uppercase;
    color: var(--author-blue);
  }
</style>
</head>
<body>
  <main class="canvas">
    <article class="book-cover">
      <svg class="title-banner" viewBox="0 0 486 245" aria-hidden="true">
        <polygon points="0,0 486,0 243,245" fill="var(--cover-red)"/>
      </svg>
      <h1 class="book-title">KITE</h1>
      <div class="tribe-figures" role="img" aria-label="Three stylised red tribal masks side by side, each wearing a necktie, the centre one with a blue tie and collar"></div>
      <p class="book-subtitle">Turning Crews into Clans</p>
      <p class="book-author">Marla Voskin</p>
    </article>
  </main>
</body>
</html>
```